Country House in Italy Needs a Business Card Design

We need a business card design for “Casale del Ruscello”, a modern concept of a Farm Holidays/Country House to be opened in central Italy.
Attached is the company logo you did for us in the past.
Please
- create a double-sided business card design
- on the back I would like to have the logo
- on the front the copy
Copy on card:
o Casale del Ruscello
o Address: Via Fontalba, 14
Cingoli (MC), Italy
o Website: www.casaledelruscello.it
o Email: info@casaledelruscello.it
o my name : Lucilla
o my mobile phone number: +39 347 8124591
In the distribution of information keep in mind the possible inclusion also of a landline telephone number (currently not available / existing).
WE WOULD LIKE TO HAVE A MODERN, PROFFESIONAL, OUT OF THE BOX BUSINESS CARD. BE AS CREATIVE AS YOU WOULD LIKE.

```html
<!DOCTYPE html>
<html lang="en">
<head>
<meta charset="utf-8">
<title>Casale del Ruscello – Business Card</title>
<link rel="stylesheet" href="https://fonts.googleapis.com/css2?family=Archivo:wght@800&family=Arimo:wght@400&family=Tinos:wght@400&display=swap">
<style>
  :root {
    --page-bg: #e8e8e9;
    --card-white: #ffffff;
    --brand-orange-dark: #dc6530;
    --brand-orange-light: #f39060;
    --brand-brown: #5e4a36;
    --brand-tan: #d9b98a;
    --ink-light: #ffffff;
    --ink-soft: rgba(255,255,255,0.88);
    --divider: rgba(255,255,255,0.7);
    --icon-cut: #e57440;
  }
  * { box-sizing: border-box; margin: 0; padding: 0; }
  html, body {
    width: 1200px; height: 800px; overflow: hidden;
    background: var(--page-bg);
  }
  .canvas {
    position: relative; width: 1200px; height: 800px;
    display: flex; align-items: center; justify-content: center; gap: 60px;
  }
  .card {
    width: 510px; height: 300px; position: relative; flex: none;
    box-shadow: 0 6px 18px rgba(0,0,0,0.12);
  }

  /* Back side – logo */
  .card--back {
    background: var(--card-white);
    display: flex; flex-direction: column; align-items: center; justify-content: center; gap: 18px;
  }
  .brand-mark {
    width: 92px; height: 92px; border-radius: 50%;
    background: var(--brand-tan);
  }
  .brand-name {
    font-family: "Tinos", "Times New Roman", serif;
    font-weight: 400; font-size: 36px; color: var(--brand-brown);
    letter-spacing: 0.5px; white-space: nowrap;
  }

  /* Front side – copy */
  .card--front {
    background: linear-gradient(200deg, var(--brand-orange-light) 0%, var(--brand-orange-dark) 100%);
    color: var(--ink-light);
    font-family: "Arimo", Arial, sans-serif;
  }
  .front-brand {
    position: absolute; left: 0; top: 0; width: 200px; height: 300px;
    display: flex; flex-direction: column; align-items: center; justify-content: center; gap: 14px;
    padding-top: 60px;
  }
  .front-brand__dot {
    width: 70px; height: 70px; border-radius: 50%; background: var(--ink-light);
  }
  .front-brand__name {
    font-size: 14px; color: var(--ink-light); white-space: nowrap;
  }
  .divider {
    position: absolute; left: 200px; top: 40px; width: 1px; height: 220px;
    background: var(--divider);
  }
  .contact {
    position: absolute; left: 232px; top: 30px; right: 16px;
  }
  .contact__name {
    font-family: "Archivo", "Arial Black", sans-serif; font-weight: 800;
    font-size: 34px; line-height: 1; letter-spacing: -0.5px;
  }
  .contact__role {
    font-size: 12px; color: var(--ink-soft); margin: 4px 0 0 14px;
  }
  .contact__list { list-style: none; margin-top: 18px; }
  .contact__item {
    display: flex; align-items: flex-start; gap: 16px;
    font-size: 13px; line-height: 1.3; color: var(--ink-soft);
    margin-bottom: 14px; white-space: nowrap;
  }
  .contact__icon { width: 22px; height: 18px; flex: none; }
</style>
</head>
<body>
<main class="canvas">
  <section class="card card--back" aria-label="Card back">
    <span class="brand-mark" aria-hidden="true"></span>
    <h1 class="brand-name">Casale del Ruscello</h1>
  </section>

  <section class="card card--front" aria-label="Card front">
    <div class="front-brand">
      <span class="front-brand__dot" aria-hidden="true"></span>
      <span class="front-brand__name">Casale del Ruscello</span>
    </div>
    <div class="divider" aria-hidden="true"></div>
    <div class="contact">
      <h2 class="contact__name">Lucilla</h2>
      <p class="contact__role">Position</p>
      <ul class="contact__list">
        <li class="contact__item">
          <svg class="contact__icon" viewBox="0 0 22 18" aria-hidden="true">
            <rect x="1" y="3" width="20" height="13" fill="#fff"/>
            <path d="M1 3 L11 11 L21 3" fill="none" stroke="var(--icon-cut)" stroke-width="1.4"/>
          </svg>
          <span>info@casaledelruscello.it</span>
        </li>
        <li class="contact__item">
          <svg class="contact__icon" viewBox="0 0 22 18" aria-hidden="true">
            <rect x="6" y="0.5" width="10" height="17" rx="2" fill="none" stroke="#fff" stroke-width="1.5"/>
            <circle cx="11" cy="14.5" r="1" fill="#fff"/>
          </svg>
          <span>+39 347 8124591</span>
        </li>
        <li class="contact__item">
          <svg class="contact__icon" viewBox="0 0 22 18" aria-hidden="true">
            <path d="M11 17 C7 11 5.5 9 5.5 6.5 A5.5 5.5 0 0 1 16.5 6.5 C16.5 9 15 11 11 17 Z" fill="#fff"/>
            <circle cx="11" cy="6.5" r="2" fill="var(--icon-cut)"/>
          </svg>
          <span>Via Fontalba, 14<br>62034 Valdoria (MC), Italy</span>
        </li>
        <li class="contact__item">
          <svg class="contact__icon" viewBox="0 0 22 18" aria-hidden="true">
            <rect x="2" y="1" width="18" height="12" rx="1" fill="#fff"/>
            <rect x="9" y="13" width="4" height="3" fill="#fff"/>
            <rect x="6" y="16" width="10" height="1.5" fill="#fff"/>
          </svg>
          <span>www.casaledelruscello.it</span>
        </li>
      </ul>
    </div>
  </section>
</main>
</body>
</html>
```